Logo + Label Design (Men’s Grooming Brand & Product Packaging)

Design a logo and 2 oz pomade label for Brant, a modern men’s grooming brand focused on clean, high-quality, natural ingredients. The design should establish a bold, masculine, minimalist identity that can later extend to products like shaving gel and body wash.

Key Requirements

Create a primary logo for “Brant” and a core label for the 2 oz pomade jar (screw-top).

Use a clean, modern style — masculine, confident, and approachable (think Wendel’s, Valto, Northfield Mill).

Design for 1–2 color screen printing on solid jar colors (white, black, or navy).

Avoid gradients, foil, or embossing. Must work in black & white.

Provide: vector logo, mockup of the 2 oz jar, color palette (CMYK/RGB/HEX), and font specs.

Winning design may lead to future projects (body wash, shave gel, skincare lines).

Font styles to use
Other font styles liked:
• We like the fonts and design concept in the attached mockup.

Requirements
Should not have
• We want to avoid too much writing or busy designs. We want to avoid having graphics/illustrations embedded in the logo if they will cause the brand to look less classy or sophisticated. We also want the design to look simple and all-American (e.g. Pellham and Stroud, Tall Pine, The BRIM, etc). We’d like to give a Kessler & Dunmore vibe that feels classy and high end.

```html
<!DOCTYPE html>
<html lang="en">
<head>
<meta charset="utf-8">
<title>Brant Hair Pomade – Logo and 2 oz Label</title>
<link href="https://fonts.googleapis.com/css2?family=Archivo:wght@400;800&family=Fira+Sans+Condensed:wght@500;600&display=swap" rel="stylesheet">
<style>
  :root {
    --paper: #ececec;
    --ink: #0b0b0b;
    --jar: #121212;
    --jar-edge: #1c1c1c;
    --label-text: #e4e4e4;
    --mark-light: #d6d6d6;
    --ghost: #2b2b2b;
    --accent: #2c52a8;
    --accent-soft: #6a8fc6;
  }
  * { box-sizing: border-box; margin: 0; padding: 0; }
  html, body { width: 1157px; height: 1200px; overflow: hidden; }
  body {
    background: var(--paper);
    font-family: "Archivo", sans-serif;
    position: relative;
  }

  /* Primary logo */
  .primary-logo {
    position: absolute; top: 95px; left: 0; width: 1157px;
    display: flex; flex-direction: column; align-items: center;
    color: var(--ink);
  }
  .wordmark {
    font-family: "Archivo", sans-serif;
    font-weight: 800;
    font-size: 190px; line-height: 1; letter-spacing: -6px;
    text-transform: lowercase;
  }
  .descriptor {
    font-family: "Archivo", sans-serif; font-weight: 400;
    text-align: right; align-self: center;
    margin-left: 260px; margin-top: 6px;
    line-height: 1.35;
  }
  .descriptor span { display: block; letter-spacing: 20px; font-size: 28px; }

  /* Lid */
  .lid {
    position: absolute; left: 408px; top: 440px;
    width: 340px; height: 340px; border-radius: 50%;
    background: var(--jar);
    border: 6px solid var(--jar-edge);
    display: flex; flex-direction: column; align-items: center; justify-content: center;
    color: var(--mark-light);
  }
  .lid .wordmark { font-size: 96px; letter-spacing: -3px; }
  .lid .descriptor { margin-left: 90px; margin-top: 2px; }
  .lid .descriptor span { font-size: 15px; letter-spacing: 9px; }

  /* Unrolled label */
  .label {
    position: absolute; left: 30px; top: 830px;
    width: 1097px; height: 320px;
    background: var(--jar);
    display: grid;
    grid-template-columns: 360px 300px 80px 1fr;
    color: var(--label-text);
    font-family: "Fira Sans Condensed", sans-serif;
    text-transform: uppercase;
  }
  .panel { padding: 36px 26px 26px; position: relative; }

  .panel-front {
    display: flex; flex-direction: column; align-items: center; justify-content: center;
    color: var(--mark-light);
  }
  .panel-front .wordmark { font-size: 100px; letter-spacing: -3px; }
  .panel-front .descriptor { margin-left: 110px; margin-top: 0; }
  .panel-front .descriptor span { font-size: 15px; letter-spacing: 9px; }
  .scent {
    font-family: "Archivo", sans-serif; font-weight: 400;
    text-transform: none; color: var(--accent);
    font-size: 17px; letter-spacing: 3px; margin-top: 22px;
  }

  .panel-title { font-size: 12px; font-weight: 600; letter-spacing: .5px; margin-bottom: 18px; }
  .panel-copy { font-size: 10.5px; font-weight: 500; line-height: 1.95; letter-spacing: .3px; }

  .hold-band {
    position: absolute; left: 26px; bottom: 62px;
    background: var(--accent-soft); color: #f2f4f8;
    font-size: 9.5px; font-weight: 600; letter-spacing: .5px;
    padding: 5px 12px; width: 190px;
  }
  .net-weight {
    position: absolute; left: 60px; bottom: 22px;
    font-size: 11px; font-weight: 500; line-height: 1.1; text-align: center;
  }

  .panel-ghost {
    display: flex; align-items: center; justify-content: center;
  }
  .ghost-name {
    writing-mode: vertical-rl;
    font-family: "Archivo", sans-serif; font-weight: 800;
    text-transform: lowercase;
    font-size: 70px; letter-spacing: -2px; color: var(--ghost);
  }

  .care-icons { display: flex; gap: 10px; margin: 14px 0 16px; }
  .care-icons svg { width: 26px; height: 26px; }
  .maker { font-size: 10.5px; font-weight: 600; line-height: 1.7; }
</style>
</head>
<body>

<header class="primary-logo">
  <div class="wordmark">brant</div>
  <div class="descriptor"><span>HAIR</span><span>POMADE</span></div>
</header>

<section class="lid" aria-label="Jar lid">
  <div class="wordmark">brant</div>
  <div class="descriptor"><span>HAIR</span><span>POMADE</span></div>
</section>

<section class="label" aria-label="2 oz jar label, unrolled">
  <div class="panel panel-front">
    <div class="wordmark">brant</div>
    <div class="descriptor"><span>HAIR</span><span>POMADE</span></div>
    <div class="scent">Fresh &amp; Clean</div>
  </div>

  <div class="panel panel-directions">
    <h2 class="panel-title">Directions</h2>
    <p class="panel-copy">Melt small amount of pomade between hands before massaging into damp hair (for sleeker look) or dry hair (for more texture). Style as desired. For external use only. Avoid contact with eyes. If irritation occurs, discontinue use.</p>
    <div class="hold-band">Medium hold – matte finish</div>
    <div class="net-weight">Net wt<br>2 oz (57 g).</div>
  </div>

  <div class="panel panel-ghost" aria-hidden="true">
    <span class="ghost-name">brant</span>
  </div>

  <div class="panel panel-ingredients">
    <h2 class="panel-title">Ingredients</h2>
    <p class="panel-copy">Butyrospermum parkii (shea butter), cera alba (beeswax), polyglycerol-3 beeswax (cera bellina), caprylic/capric triglyceride (fractionated coconut oil), tocopherol (vitamin E), fragrance (parfum)</p>
    <div class="care-icons" aria-label="Care symbols">
      <svg viewBox="0 0 26 26" fill="none" stroke="currentColor" stroke-width="1.6"><circle cx="7" cy="5" r="2"/><path d="M7 8v8M4 11h6M12 10h9l-1.5 13h-6z"/></svg>
      <svg viewBox="0 0 26 26" fill="none" stroke="currentColor" stroke-width="2"><circle cx="13" cy="13" r="11"/><path d="M7 14a6 6 0 0 1 10-5M19 12a6 6 0 0 1-10 5"/></svg>
      <svg viewBox="0 0 26 26" fill="currentColor"><path d="M13 2c2 5 8 8 8 15a8 8 0 0 1-16 0c0-4 3-6 4-9 1 3 2 4 3 4 1-3 0-6 1-10z"/></svg>
      <svg viewBox="0 0 26 26" fill="none" stroke="currentColor" stroke-width="1.5"><path d="M3 12h20v10H3zM4 10l16-6"/><text x="8" y="20" font-size="6" fill="currentColor" stroke="none">6M</text></svg>
    </div>
    <p class="maker">Manufactured by:<br>Brant Grooming Co., Millbrook, OH<br>44021<br>Visit us at brantgrooming.com</p>
  </div>
</section>

</body>
</html>
```